Branding Assistance needed for Business Consultantcy expansion

Looking for some key branding components to assist with the expansion of our company into business consultancy work.
Existing company is an Accountancy firm (Ferrowind Accountants) and we have set up a new Company (TrellQuoran) which is the Business Consultancy arm.
We offer an Accountancy & Business Consultancy service and believe strongly in helping people achieve their dreams through business success.

Ferrowind focusses on Taxation, Compliance & Restructure work.
TrellQuoran will focus on Business Development and Enhancement (Sales, Marketing, Systems & Planning)

I need to develop some General branding Tools across the 2 x arms.
We are all about fixing Business Problems.

Specifically I need:
1 x New Logo Design (For TrellQuoran)
4 x Product/Feature Icon Designs
1 x Pull Up Banner Design

Logo Design
This is purely a new Logo for Trellquoran.

4 x Icon Designs..
...that I can use on business cards, posters signs etc.
The aim of the Icons is to have a consistent look and feel around our messaging.
If it helps, the basic messaging we are trying to get across is:
We help your business Perform
So you can create Wealth and stability
So to impact your Lifestyle
And enable you to reach your Goals & Dreams
The words to go with each Icon are (in brackets I have put my iinitial ideas of what the icon might represent):
Performance (Graph/Chart on the increase?)
Wealth (Dollar sign?)
Lifestyle (Family time?)
Dreams (future/sunset?)
(I have attached some images that may help with the concept but feel free to go left field)

Pull Up Banner Design
Looking for a great design for a Pull up Banner measuring 850mm wide and 2000mm high.

The current text we have in mind is... (But will probably change)

“Less time working…more time living.”

“What would you rather be doing?” (MAIN MESSAGE)
4 Icons
“Let us take you there”

Then include some imagery for Success, Performance, Family, Goals/Dreams, Holidays??

Our Logo for the Accountancy side of the business (Ferrowind Accountants) is traditionally Blue with complementing colours usually being Gold and lighter browns.
On the business consultancy (TrellQuoran) side of things we will probably lend itself to greens and browns. (See sample Logo)
But happy to consider new pallets.
Updates

I have increased the budget for 1st prize to $300

Project Deadline Extended
Reason: Extending the deadline to assist with everyone having enough time to submit designs.

I am extending deadline until tommorrow to give everyone a chance to finish off their works.
Hope this helps.

Project Deadline Extended
Reason: I am extending deadline until tommorrow to give everyone a chance to finish off their works. Hope this helps.

Target Market(s)

Small to Medium Business Owners (usually Family owned businesses)

Industry/Entity Type

Business

Requirements
Must have
• TrellQuoran Logo
Must capture the essence of the name and what we do. TrellQuoran (as in Landscaping your business) Tag line would be "Revive, Redesign, Revitalize your Business"

Icons
Consistency across the 4 icons, so if a caricature icon of a dollar sign is used with a Bold Border, then same concept carried through on other Icons.

Pull Up Banner
To fit dimensions 850mm by 2000mm
Note: please allow for 30mm bleed at Top and 150mm bleed at bottom.
Should not have
• Should not be just another "corporate" look and feel.
Needs to be vibrant and stand out.

```html
<!DOCTYPE html>
<html lang="en">
<head>
<meta charset="utf-8">
<title>TrellQuoran Pull Up Banner</title>
<link href="https://fonts.googleapis.com/css2?family=Questrial&display=swap" rel="stylesheet">
<style>
  :root {
    --green: #8dc63f;
    --blue: #2797be;
    --white: #ffffff;
    --photo-light: #eef2ea;
    --photo-mid: #c9cfb8;
    --photo-warm: #9a8a74;
  }
  html, body {
    margin: 0;
    padding: 0;
    width: 1200px;
    height: 2821px;
    overflow: hidden;
    background: var(--white);
  }
  .banner {
    position: relative;
    width: 1200px;
    height: 2821px;
    overflow: hidden;
    font-family: "Questrial", "Century Gothic", sans-serif;
  }
  .top-rule {
    position: absolute;
    left: 0; top: 0;
    width: 1200px; height: 14px;
    background: var(--blue);
  }
  .brand-box {
    position: absolute;
    left: 730px; top: 0;
    width: 470px; height: 230px;
    background: var(--blue);
    color: var(--white);
    display: flex;
    flex-direction: column;
    justify-content: center;
    align-items: center;
  }
  .brand-name {
    font-size: 66px;
    letter-spacing: -1px;
    line-height: 1;
  }
  .brand-tagline {
    font-size: 13px;
    margin-top: 10px;
    letter-spacing: 0.3px;
  }
  .headline {
    position: absolute;
    left: 0; top: 0;
    width: 1200px; height: 1530px;
  }
  .headline text {
    font-family: "Questrial", "Century Gothic", sans-serif;
  }
  .question-band {
    position: absolute;
    left: 0; top: 1218px;
    width: 1157px; height: 287px;
    background: var(--green);
  }
  .question {
    position: absolute;
    left: 100px; top: 1268px;
    margin: 0;
    color: var(--white);
    font-weight: 400;
    font-size: 92px;
    line-height: 96px;
    letter-spacing: -4px;
  }
  .divider {
    position: absolute;
    left: 0; top: 1505px;
    width: 1200px; height: 18px;
    background: var(--blue);
  }
  .lifestyle-photo {
    position: absolute;
    left: 0; top: 1523px;
    width: 1200px; height: 1298px;
    background: linear-gradient(160deg, var(--photo-light) 0%, var(--photo-mid) 55%, var(--photo-warm) 100%);
  }
</style>
</head>
<body>
<div class="banner">
  <div class="top-rule"></div>

  <div class="brand-box">
    <div class="brand-name">TrellQuoran</div>
    <div class="brand-tagline">Revive, Redesign, Revitalize Your Business</div>
  </div>

  <svg class="headline" viewBox="0 0 1200 1530" xmlns="http://www.w3.org/2000/svg">
    <rect class="accent-column" x="908" y="990" width="249" height="240" fill="var(--green)"/>
    <text x="79" y="392" font-size="96" fill="var(--green)" letter-spacing="-4" textLength="442" lengthAdjust="spacingAndGlyphs">Less time</text>
    <text x="79" y="540" font-size="190" fill="var(--blue)" letter-spacing="-6" textLength="940" lengthAdjust="spacingAndGlyphs">working…</text>
    <text x="670" y="738" font-size="108" fill="var(--blue)" letter-spacing="-5" textLength="487" lengthAdjust="spacingAndGlyphs">More time</text>
    <text x="100" y="995" font-size="460" fill="var(--green)" letter-spacing="-18" textLength="1057" lengthAdjust="spacingAndGlyphs">Living</text>
    <path class="descender-swoosh" d="M1150 945 C1150 1060 1080 1090 975 1085" fill="none" stroke="var(--blue)" stroke-width="44" stroke-linecap="butt"/>
  </svg>

  <div class="question-band"></div>
  <h1 class="question">What would you<br>rather be doing?</h1>

  <div class="divider"></div>

  <div class="lifestyle-photo" role="img" aria-label="Photograph of a smiling couple sharing a meal together at home in a bright room"></div>
</div>
</body>
</html>
```